The Larkspur Whiskey & Coffee - Bar Menu

The Larkspur is a speakeasy style coffee and whiskey bar. Upscale with design elements tying in both prohibition era elegance and modern touches.

Black and Gold are our colors. (see logo)

We would need a 8 page menu- front and back. 4.24 in x 11 in for each page. The pages would be:

Intro page
Food/Dessert
Cocktails x 2 pages
Wine- Glass Pour
Wine- Bottle only
Beer
Non-Alcoholic Beverages

Attached is the menu cocktails and food/non alcoholic.

We need an editable format as this menu would be constantly changing.

UPDATE: The owner would potentially like to see the use of the original floor plans incorporated into the menu design. I have uploaded those to this brief.

UPDATE: I have added some photos that show the style the owner would like the writing to be displayed.

Requirements
Should not have
• No pictures of wine or beer or other images. Clipart could be fine, but we want to showcase class and an upscale vibe.

```html
<!DOCTYPE html>
<html lang="en">
<head>
<meta charset="utf-8">
<title>The Larkspur Whiskey &amp; Coffee – Food &amp; Cocktails</title>
<link href="https://fonts.googleapis.com/css2?family=Bebas+Neue&family=Overlock:wght@400;700&display=swap" rel="stylesheet">
<style>
  :root {
    --gold: #dcbf4e;
    --ink: #0a0a0a;
    --paper: #ffffff;
    --fold: #3a3a3a;
    --plan-a: #1c1a10;
    --plan-b: #2a2513;
  }
  * { margin: 0; padding: 0; box-sizing: border-box; }
  html, body { width: 1200px; height: 1200px; overflow: hidden; background: var(--paper); }
  .menu-spread {
    position: absolute; left: 137px; top: 0; width: 926px; height: 1200px;
    background: var(--ink); color: var(--gold);
    font-family: "Overlock", sans-serif;
  }
  .fold { position: absolute; left: 462px; top: 0; width: 1px; height: 1200px; background: var(--fold); }
  .page-title, .section-title, .spirit-title {
    position: absolute; font-family: "Bebas Neue", sans-serif; font-weight: 400; line-height: 1;
  }
  .page-title { font-size: 62px; top: 26px; transform: translateX(-50%); letter-spacing: 0.5px; }
  .page-title.food { left: 231px; }
  .page-title.cocktails { left: 695px; }
  .section-title.dessert { font-size: 66px; left: 231px; top: 876px; transform: translateX(-50%); }
  .spirit-title { font-size: 40px; left: 520px; }
  .item { position: absolute; }
  .food-item { left: 57px; width: 362px; }
  .item-head { display: flex; justify-content: space-between; align-items: baseline; }
  .item-name { font-weight: 700; font-size: 25.5px; line-height: 28px; white-space: nowrap; }
  .item-price { font-weight: 700; font-size: 25.5px; line-height: 28px; }
  .item-desc { font-size: 16px; line-height: 18px; white-space: nowrap; }
  .drink { left: 520px; width: 380px; }
  .drink .item-desc { line-height: 18.5px; }
  .drink .item-desc.loose { line-height: 20px; }
  .plan-art { position: absolute; background: linear-gradient(135deg, var(--plan-a), var(--plan-b)); }
</style>
</head>
<body>
<main class="menu-spread">
  <div class="fold"></div>

  <h1 class="page-title food">Food</h1>
  <h1 class="page-title cocktails">Cocktails</h1>

  <section class="food-list">
    <div class="item food-item" style="top:168px">
      <div class="item-head"><span class="item-name">Bone marrow</span><span class="item-price">$20</span></div>
      <p class="item-desc">Bone marrow roasted with sea salt and served with<br>warm tortillas</p>
    </div>
    <div class="item food-item" style="top:242px">
      <div class="item-head"><span class="item-name">Charcuterie board</span><span class="item-price">$25</span></div>
      <p class="item-desc">Assorted artisan meats and cheeses, nuts, and fruits</p>
    </div>
    <div class="item food-item" style="top:297px">
      <div class="item-head"><span class="item-name">Hummus, Veggie, &amp; Pita</span><span class="item-price">$16</span></div>
      <p class="item-desc">Assorted vegetables with warm pita and roasted<br>garlic hummus</p>
    </div>
    <div class="item food-item" style="top:376px">
      <div class="item-head"><span class="item-name">Lamb Chops</span><span class="item-price">$18</span></div>
      <p class="item-desc">Lamb chops broiled with rosemary</p>
    </div>
    <div class="item food-item" style="top:434px">
      <div class="item-head"><span class="item-name">Tuna Tower</span><span class="item-price">$17</span></div>
      <p class="item-desc">Fresh tuna served with white rice, avocado and spice</p>
    </div>
    <div class="item food-item" style="top:496px">
      <div class="item-head"><span class="item-name">Lettuce Wrap - Walnut Shrimp</span><span class="item-price">$13</span></div>
      <p class="item-desc">Honey walnut aioli coated shrimp and lettuce cups<br>with a candied walnut</p>
    </div>
  </section>

  <div class="plan-art" style="left:218px; top:618px; width:201px; height:147px" role="img" aria-label="Floor plan drawing of a dining table with six chairs"></div>

  <h2 class="section-title dessert">Dessert</h2>
  <section class="dessert-list">
    <div class="item food-item" style="top:1025px">
      <div class="item-head"><span class="item-name">Tart</span></div>
      <p class="item-desc">Your choice of apple or berry with vanilla ice cream</p>
    </div>
    <div class="item food-item" style="top:1083px">
      <div class="item-head"><span class="item-name">Cheesecake</span></div>
      <p class="item-desc">Chocolate or strawberry drizzle</p>
    </div>
  </section>

  <section class="cocktail-list">
    <h2 class="spirit-title" style="top:168px">Vodka</h2>
    <div class="item drink" style="top:234px">
      <div class="item-name">The Affair</div>
      <p class="item-desc">Vodka (strawberry/orange infusion), Lemon Oleo<br>Saccahrum, PeaFlower Gin Float(Blue) (N&amp;N)</p>
    </div>
    <div class="item drink" style="top:309px">
      <div class="item-name">Bootleggers Gold</div>
      <p class="item-desc">Vodka, Yellow Vervaine, Pineapple, Lime Juice,<br>Simple Syrup, Lemon Zest</p>
    </div>

    <h2 class="spirit-title" style="top:401px">Tequila</h2>
    <div class="item drink" style="top:472px">
      <div class="item-name">The Mayan</div>
      <p class="item-desc">Casa Ruelo Blanco, Raicilla (non-peaty Mezcal), Green<br>Vervaine, Pistachio Liqueur, Olive, Lime</p>
    </div>
    <div class="item drink" style="top:549px">
      <div class="item-name">Toreador*</div>
      <p class="item-desc">Blanco, Mezcal, Apricot Cordial, Lime Juice, GrapeFruit<br>oil(oleo), Mezcal Mist</p>
    </div>

    <h2 class="spirit-title" style="top:641px">Rum</h2>
    <div class="item drink" style="top:713px">
      <div class="item-name">Smugglers Inlet**</div>
      <p class="item-desc loose">Rum (Cuban), Pomegranite Liqueur, Lemon Juice,<br>Macadamia Orgeat, Cocoa Bitters (Eggwhite)</p>
    </div>
    <div class="item drink" style="top:796px">
      <div class="item-name">Mary Pembrook*</div>
      <p class="item-desc">Rum (Blanco Cuban), Pineapple, Maraschino Liqueur,<br>Grenadine</p>
    </div>
    <div class="item drink" style="top:871px">
      <div class="item-name">Roy Rum Runner (Local)</div>
      <p class="item-desc">Rum (Blanco), Rhum Agricole (non-peat Mezcal) Lime<br>Juice, Simple Syrup w/in season fruit</p>
    </div>
  </section>

  <div class="plan-art" style="left:497px; top:987px; width:395px; height:177px" role="img" aria-label="Floor plan drawing of a lounge with sectional sofa, side table and bar counter"></div>
</main>
</body>
</html>
```